Business Card Design

New business card design

Target Market(s)

Residential & Commercial Property Managers

Industry/Entity Type

Plumbing Services

Contact Information for Business Card

Name - Owen Tredgold, title - Director, Phone Number - 0431 862 507, email - owen@rvb-plumbing.com.au, Company ABN - 73 215 904 386,

Font styles to use
Sans Serif

Colors
0054AA
0677BA
7BADD7
CADEEF
E8F1F8

```html
<!DOCTYPE html>
<html lang="en">
<head>
<meta charset="utf-8">
<title>RVB Plumbing Services – Business Card</title>
<link rel="stylesheet" href="https://fonts.googleapis.com/css2?family=Arimo:wght@400;700&display=swap">
<style>
  :root {
    --canvas: #e8f1f8;
    --card-dark: #1d2329;
    --card-dark-name: #2f3a46;
    --card-light: #ffffff;
    --ink: #1b1f24;
    --ink-soft: #3a3f45;
    --brand-deep: #0054aa;
    --brand-mid: #0677ba;
    --brand-light: #7badd7;
    --brand-pale: #cadeef;
    --shadow: rgba(0, 40, 80, 0.18);
  }
  * { margin: 0; padding: 0; box-sizing: border-box; }
  html, body {
    width: 1200px; height: 874px; overflow: hidden;
    background: var(--canvas);
    font-family: "Arimo", Arial, sans-serif;
  }
  .stage { position: relative; width: 1200px; height: 874px; }
  .card {
    position: absolute; left: 270px; width: 660px; height: 402px;
    border-radius: 22px; overflow: hidden;
    box-shadow: 0 10px 28px var(--shadow);
  }
  .card--back { top: 24px; background: var(--card-dark); }
  .card--front { top: 456px; background: var(--card-light); }

  .brand-name { position: absolute; font-weight: 700; line-height: 1; white-space: nowrap; }
  .card--back .brand-name {
    left: 0; right: 0; top: 178px; text-align: center;
    font-size: 46px; color: var(--card-dark-name);
  }
  .card--front .brand-name {
    left: 40px; top: 48px; font-size: 32px; color: var(--brand-deep);
  }

  .person { position: absolute; left: 40px; top: 160px; }
  .person__name { font-size: 28px; font-weight: 700; color: var(--ink); }
  .person__title { font-size: 16px; color: var(--brand-mid); margin-top: 4px; }

  .contact { position: absolute; left: 40px; top: 262px; list-style: none; }
  .contact__item {
    display: flex; align-items: center; gap: 10px;
    font-size: 17px; color: var(--ink-soft); line-height: 28px;
  }
  .contact__icon { width: 14px; height: 14px; flex: none; }
  .contact__abn { margin-top: 4px; }

  .feature-block {
    position: absolute; right: 58px; top: 100px;
    width: 230px; height: 230px; border-radius: 24px;
    background: linear-gradient(160deg, var(--brand-light), var(--brand-mid));
  }
</style>
</head>
<body>
<main class="stage">
  <section class="card card--back" aria-label="Business card back">
    <p class="brand-name">RVB Plumbing Services</p>
  </section>

  <section class="card card--front" aria-label="Business card front">
    <p class="brand-name">RVB Plumbing Services</p>

    <div class="person">
      <p class="person__name">Owen Tredgold</p>
      <p class="person__title">Director</p>
    </div>

    <ul class="contact">
      <li class="contact__item">
        <svg class="contact__icon" viewBox="0 0 24 24" aria-hidden="true">
          <path fill="#1b1f24" d="M6.6 10.8a15.1 15.1 0 0 0 6.6 6.6l2.2-2.2c.3-.3.7-.4 1-.2 1.1.4 2.3.6 3.6.6.6 0 1 .4 1 1V20c0 .6-.4 1-1 1A17 17 0 0 1 3 4c0-.6.4-1 1-1h3.5c.6 0 1 .4 1 1 0 1.3.2 2.5.6 3.6.1.3 0 .7-.2 1z"/>
        </svg>
        <span>0431 862 507</span>
      </li>
      <li class="contact__item">
        <svg class="contact__icon" viewBox="0 0 24 24" aria-hidden="true">
          <path d="M2 5h20v14H2z M3.5 6.5 12 13l8.5-6.5" fill="none" stroke="#1b1f24" stroke-width="2"/>
        </svg>
        <span>owen@rvb-plumbing.com.au</span>
      </li>
      <li class="contact__item contact__abn">
        <span>ABN - 73 215 904 386</span>
      </li>
    </ul>

    <div class="feature-block" role="img" aria-label="Large blue decorative brand graphic"></div>
  </section>
</main>
</body>
</html>
```